A UK based Lettings and Property Management Company - Maple Crest Property

Maple Crest Property rents and manages properties on behalf of owners in Liverpool, UK. We are looking for a clean, fresh modern design which incororates our logo.

In terms of pages we initially require:

Home
Lettings
Property Management
Landlords
Tenants
About
Contact

In would like to use colours compatible with the logo

Target Market(s)

People looking to rent property
Owners looking to use our services to let their property

Industry/Entity Type

Property

Contact Information for Business Card

Logo prominent on one side
Address to be edited by us as we are moving premises in October
Name Gavin Holloway
Tel number 0151 486 2037
e-mail gavin@maplecrestproperty.co.uk

Font styles to use
Sans Serif

Colors

Designer to choose colors to be used in the design.

Requirements
Must have
• Clean lines
• Fresh
• Easy navigation
• Easy editing
• Data capture

```html
<!DOCTYPE html>
<html lang="en">
<head>
<meta charset="utf-8">
<title>Maple Crest Property – Lettings and Property Management</title>
<link rel="stylesheet" href="https://fonts.googleapis.com/css2?family=Mulish:wght@400;600;700&family=Open+Sans:ital,wght@0,400;0,600;1,400&display=swap">
<style>
:root{
  --navy:#101040;
  --navy-deep:#0c0c33;
  --charcoal:#323232;
  --footer:#2a2a2a;
  --ink:#222;
  --grey:#7a7a7a;
  --light:#eeeeee;
  --white:#fff;
  --line:#d8d8d8;
}
*{margin:0;padding:0;box-sizing:border-box}
html,body{width:1200px;height:3103px;overflow:hidden}
body{font-family:"Open Sans",Arial,sans-serif;color:var(--ink);background:var(--white);position:relative}
h1,h2,h3,h4,.nav,.logo-name,.btn{font-family:"Mulish",Arial,sans-serif}
section,header,footer{position:absolute;left:0;width:1200px}

/* header */
.site-header{top:0;height:99px;background:var(--white)}
.logo{position:absolute;left:120px;top:26px;display:flex;align-items:center;gap:12px}
.logo-square{width:46px;height:46px;background:var(--navy)}
.logo-name{font-size:27px;font-weight:700;color:var(--navy);line-height:1;width:240px;letter-spacing:.5px}
.nav{position:absolute;right:120px;top:40px;display:flex;gap:24px;font-size:15.5px;color:#666}
.nav .active{color:var(--navy);font-weight:600}

/* hero */
.hero{top:99px;height:553px}
.hero-photo{position:absolute;inset:0;background:linear-gradient(100deg,#b79a78 0%,#d9c6a8 35%,#c9b397 55%,#a98a6c 80%,#8b6e56 100%)}
.hero-title{position:absolute;left:120px;top:266px;color:var(--white);font-size:34px;font-weight:600;line-height:48px;letter-spacing:.5px}
.hero-arrow{position:absolute;top:245px}
.hero-badge{position:absolute;left:560px;top:522px;width:80px;height:80px;background:var(--white);box-shadow:0 1px 6px rgba(0,0,0,.25);display:flex;align-items:center;justify-content:center}
.hero-badge span{width:56px;height:56px;background:var(--navy)}

/* about */
.about{top:652px;height:370px;text-align:center}
.about h2{margin-top:82px;font-size:30px;font-weight:600;color:var(--ink)}
.about p{width:880px;margin:22px auto 0;font-size:14px;line-height:27px;color:var(--grey)}
.btn{display:inline-block;border:2px solid #444;color:var(--ink);font-size:14px;font-weight:600;padding:9px 0;text-align:center;text-transform:uppercase}
.about .btn{width:155px;margin-top:30px}

/* services */
.services{top:1022px;height:435px}
.service{position:absolute;top:0;height:435px;text-align:center;color:var(--white)}
.service-pm{left:0;width:610px;background:var(--charcoal)}
.service-let{right:0;width:610px;background:var(--navy);clip-path:polygon(12px 0,100% 0,100% 100%,18px 100%)}
.service-pm .inner{position:absolute;left:215px;width:240px}
.service-let .inner{position:absolute;left:127px;width:490px}
.icon-box{width:120px;height:110px;border:1.5px solid rgba(255,255,255,.7);margin:72px auto 0;display:flex;align-items:center;justify-content:center}
.service h3{font-size:24px;font-weight:600;margin-top:36px;letter-spacing:.5px}
.service p{font-size:14px;line-height:26px;margin:10px auto 0;width:420px;color:#d8d8e0}
.service .btn{border-color:var(--white);color:var(--white);width:140px;margin-top:22px}
.service-pm .inner{left:55px;width:560px}

/* featured */
.featured{top:1457px;height:500px}
.featured h2{position:absolute;left:128px;top:64px;font-size:24px;font-weight:600}
.card{position:absolute;top:115px;width:228px;height:303px;border:1px solid var(--line);background:var(--white)}
.card-photo{height:180px}
.card h4{font-family:"Open Sans",Arial,sans-serif;font-size:14px;font-weight:400;margin:18px 0 0 22px}
.card p{font-size:11px;line-height:19px;color:var(--grey);margin:6px 20px 0 22px}
.card a{display:block;margin:8px 0 0 22px;font-size:12px;font-weight:700;color:var(--navy);text-decoration:none}

/* testimonials */
.testimonials{top:1957px;height:325px;background:linear-gradient(180deg,#1b1b55 0%,#12124a 50%,#0d0d3a 100%)}
.testimonials h2{text-align:center;color:var(--white);font-size:30px;font-weight:600;margin-top:60px}
.avatar{position:absolute;left:188px;top:118px;width:120px;height:120px;border-radius:50%;border:5px solid var(--white);background:linear-gradient(160deg,#d8c2ad,#9b8573)}
.quote{position:absolute;left:335px;top:130px;width:660px;color:#e4e4f0;font-size:15px;line-height:25px;font-style:italic}
.quote cite{display:block;margin-top:8px;font-size:14px;font-weight:600;font-style:italic;color:var(--white)}
.dots{position:absolute;left:570px;top:263px;display:flex;gap:6px}
.dots span{width:11px;height:11px;border-radius:50%;border:2px solid var(--white)}
.dots span.on{background:var(--white)}

/* landlords */
.landlords{top:2282px;height:445px;background:var(--light);text-align:center}
.landlords h2{font-size:30px;font-weight:600;color:var(--navy);margin-top:40px}
.landlord{position:absolute;top:95px;width:220px;text-align:center}
.landlord h4{font-size:17px;font-weight:600;color:#333;margin-top:6px}
.landlord p{font-size:11px;line-height:19px;color:var(--grey);margin-top:4px}

/* footer */
.site-footer{top:2727px;height:376px;background:var(--footer);color:#ddd}
.col{position:absolute;top:58px}
.col h4{font-size:17px;font-weight:600;color:var(--white);letter-spacing:.5px;margin-bottom:6px}
.col li{list-style:none;font-size:14px;line-height:28px;color:#ccc}
.social{display:flex;gap:8px;margin-top:10px}
.social span{width:36px;height:36px;border-radius:50%;background:#555}
.contact-line{display:flex;gap:10px;font-size:14px;line-height:28px;color:#ccc}
.contact-line svg{margin-top:6px;flex:none}
.rule{position:absolute;left:126px;right:110px;top:303px;border-top:1px solid #4a4a4a}
.copyright{position:absolute;top:330px;width:100%;text-align:center;font-size:12px;color:#aaa}
</style>
</head>
<body>

<header class="site-header">
  <div class="logo"><span class="logo-square"></span><span class="logo-name">MAPLE CREST PROPERTY</span></div>
  <nav class="nav">
    <span class="active">Home</span><span>Lettings</span><span>Property Management</span><span>Landlords</span><span>Tenants</span><span>About</span><span>Contact</span>
  </nav>
</header>

<section class="hero">
  <div class="hero-photo" role="img" aria-label="Letting agent handing house keys to a young couple outside a front door"></div>
  <h1 class="hero-title">LETTINGS AND PROPERTY<br>MANAGEMENT SERVICES</h1>
  <svg class="hero-arrow" style="left:78px" width="22" height="36" viewBox="0 0 22 36"><path d="M18 3 4 18l14 15" fill="none" stroke="#fff" stroke-width="3"/></svg>
  <svg class="hero-arrow" style="left:1090px" width="22" height="36" viewBox="0 0 22 36"><path d="M4 3l14 15L4 33" fill="none" stroke="#fff" stroke-width="3"/></svg>
  <div class="hero-badge"><span></span></div>
</section>

<section class="about">
  <h2>ABOUT MAPLE CREST PROPERTY</h2>
  <p>Praesent elementum elit at tellus nec ultricies sit amet porttitor mattis enim In massa libero interdum nec interdum vel blandit sed nulla In ullamcorper est eget tempor cursus neque mi consectetuer mi a ultricies massa est sed nisl Class aptent taciti sociosqu ad litora torquent per conubia nostra per inceptos hymenaeos Proin nulla arcu</p>
  <span class="btn">Read More</span>
</section>

<section class="services">
  <div class="service service-pm">
    <div class="inner">
      <div class="icon-box">
        <svg width="70" height="64" viewBox="0 0 70 64" fill="none" stroke="#fff" stroke-width="2.5" stroke-linejoin="round">
          <path d="M20 26 38 10l18 16M25 22v14h26V22"/><rect x="34" y="26" width="8" height="8"/>
          <path d="M6 44h10l10 4h12a3 3 0 0 1 0 6H26M38 54l18-8a3 3 0 0 1 4 5L40 60H16"/>
        </svg>
      </div>
      <h3>PROPERTY MANAGEMENT</h3>
      <p>Aulla In ullamcorper est eget tempor cursus neque mi consectetuer mi a ultricies massa est sed</p>
      <span class="btn">Read More</span>
    </div>
  </div>
  <div class="service service-let">
    <div class="inner">
      <div class="icon-box">
        <svg width="72" height="62" viewBox="0 0 72 62" fill="none" stroke="#fff" stroke-width="2.5" stroke-linejoin="round">
          <path d="M4 30 36 5l32 25M12 24v32h48V24M20 14V6h8v4"/>
          <circle cx="36" cy="38" r="6"/>
          <path d="M36 26v5M36 45v5M24 38h5M43 38h5M27.5 29.5l3.5 3.5M41 43l3.5 3.5M27.5 46.5 31 43M41 33l3.5-3.5"/>
        </svg>
      </div>
      <h3>LETTINGS</h3>
      <p>Aulla In ullamcorper est eget tempor cursus neque mi consectetuer mi a ultricies massa est sed</p>
      <span class="btn">Read More</span>
    </div>
  </div>
</section>

<section class="featured">
  <h2>FEATURED PROPERTY</h2>
  <article class="card" style="left:126px">
    <div class="card-photo" role="img" aria-label="Modern two-storey house with driveway at dusk" style="background:linear-gradient(180deg,#8fa7c4,#6d7e8e 55%,#b8b4ae)"></div>
    <h4>Property Tittle</h4><p>netus et malesuada fames ac turpis egestas Cras id elit Integer</p><a href="#">READ MORE</a>
  </article>
  <article class="card" style="left:368px">
    <div class="card-photo" role="img" aria-label="Large family home lit up at twilight with front lawn" style="background:linear-gradient(180deg,#3c5a86,#5a5748 55%,#4f6a3a)"></div>
    <h4>Property Tittle</h4><p>netus et malesuada fames ac turpis egestas Cras id elit Integer</p><a href="#">READ MORE</a>
  </article>
  <article class="card" style="left:608px">
    <div class="card-photo" role="img" aria-label="White detached house with green garden" style="background:linear-gradient(180deg,#9cc3e6,#e8ecef 45%,#6f9a4c)"></div>
    <h4>Property Tittle</h4><p>netus et malesuada fames ac turpis egestas Cras id elit Integer</p><a href="#">READ MORE</a>
  </article>
  <article class="card" style="left:850px">
    <div class="card-photo" role="img" aria-label="Contemporary villa with swimming pool in the evening" style="background:linear-gradient(180deg,#4a5f9c,#8a7a6e 55%,#3f7fb0)"></div>
    <h4>Property Tittle</h4><p>netus et malesuada fames ac turpis egestas Cras id elit Integer</p><a href="#">READ MORE</a>
  </article>
</section>

<section class="testimonials" role="img" aria-label="Dark blue city skyline backdrop">
  <h2>TESTIMONIALS</h2>
  <div class="avatar" role="img" aria-label="Portrait photo of the client"></div>
  <blockquote class="quote">“ Lorem ipsum dolor sit amet, consectetur adipiscing elit, sed do eiusmod tempor incididunt ut labore et dolore magna aliqua. Ut enim ad minim veniam, quis nostrud exercitation ullamco laboris nisi ut aliquip ex ea commodo consequat. Duis aute irure dolor in reprhe ”<cite>- John Doe</cite></blockquote>
  <div class="dots"><span class="on"></span><span></span><span></span></div>
</section>

<section class="landlords">
  <h2>LANDLORDS</h2>
  <svg width="0" height="0" style="position:absolute">
    <defs><linearGradient id="portrait" x1="0" y1="0" x2="0" y2="1"><stop offset="0" stop-color="#d9d9d9"/><stop offset="1" stop-color="#9a9aa2"/></linearGradient></defs>
  </svg>
  <div class="landlord" style="left:126px">
    <svg width="190" height="200" viewBox="0 0 190 200" role="img" aria-label="Landlord portrait photo"><polygon points="95,4 182,52 182,148 95,196 8,148 8,52" fill="none" stroke="#bbb" stroke-width="2"/><polygon points="95,14 173,57 173,143 95,186 17,143 17,57" fill="url(#portrait)"/></svg>
    <h4>Landlord Name</h4><p>Class aptent taciti sociosqu ad litora torquent per conubia nos</p>
  </div>
  <div class="landlord" style="left:368px">
    <svg width="190" height="200" viewBox="0 0 190 200" role="img" aria-label="Landlord portrait photo"><polygon points="95,4 182,52 182,148 95,196 8,148 8,52" fill="none" stroke="#bbb" stroke-width="2"/><polygon points="95,14 173,57 173,143 95,186 17,143 17,57" fill="url(#portrait)"/></svg>
    <h4>Landlord Name</h4><p>Class aptent taciti sociosqu ad litora torquent per conubia nos</p>
  </div>
  <div class="landlord" style="left:612px">
    <svg width="190" height="200" viewBox="0 0 190 200" role="img" aria-label="Landlord portrait photo"><polygon points="95,4 182,52 182,148 95,196 8,148 8,52" fill="none" stroke="#bbb" stroke-width="2"/><polygon points="95,14 173,57 173,143 95,186 17,143 17,57" fill="url(#portrait)"/></svg>
    <h4>Landlord Name</h4><p>Class aptent taciti sociosqu ad litora torquent per conubia nos</p>
  </div>
  <div class="landlord" style="left:854px">
    <svg width="190" height="200" viewBox="0 0 190 200" role="img" aria-label="Landlord portrait photo"><polygon points="95,4 182,52 182,148 95,196 8,148 8,52" fill="none" stroke="#bbb" stroke-width="2"/><polygon points="95,14 173,57 173,143 95,186 17,143 17,57" fill="url(#portrait)"/></svg>
    <h4>Landlord Name</h4><p>Class aptent taciti sociosqu ad litora torquent per conubia nos</p>
  </div>
</section>

<footer class="site-footer">
  <div class="col" style="left:143px"><h4>COMPANY</h4><ul><li>Home</li><li>About Us</li><li>Lettings</li><li>Property Management</li></ul></div>
  <div class="col" style="left:354px"><h4>RESOURCES</h4><ul><li>Landlords</li><li>Tenants</li><li>Contact Us</li></ul></div>
  <div class="col" style="left:536px"><h4>FOLLOW US</h4><div class="social"><span></span><span></span><span></span><span></span></div></div>
  <div class="col" style="left:786px"><h4>CONTACT US</h4>
    <div class="contact-line"><svg width="14" height="18" viewBox="0 0 14 18"><path d="M7 0a7 7 0 0 0-7 7c0 5 7 11 7 11s7-6 7-11a7 7 0 0 0-7-7zm0 10a3 3 0 1 1 0-6 3 3 0 0 1 0 6z" fill="#fff"/></svg><span>14 Harbour Row Suite 3<br>Liverpool L3 9QT</span></div>
    <div class="contact-line" style="margin-top:22px"><svg width="16" height="16" viewBox="0 0 16 16"><path d="M3 1l3 3-2 2c1 2 3 4 5 5l2-2 3 3-2 3C6 15 1 10 1 3z" fill="#fff"/></svg><span>0151 486 2037</span></div>
    <div class="contact-line"><svg width="16" height="12" viewBox="0 0 16 12"><rect width="16" height="12" rx="1" fill="#fff"/><path d="M1 1l7 6 7-6" fill="none" stroke="#2a2a2a" stroke-width="1.5"/></svg><span>info@maplecrestproperty.co.uk</span></div>
  </div>
  <div class="rule"></div>
  <p class="copyright">© 2017 Company Name &nbsp;All right reserved &nbsp;Term of Use</p>
</footer>

</body>
</html>
```